Website Design for Chef Wirra Chinese Restaurant

Chef Wirra is a new Chinese Restaurant. It offers exceptional dining experience with authentic and dynamic dishes created with quality ingredients.

A vivid website theme is required to promote this new restaurant online. Logo, menu, wine list and a few other files are attached for help with designing.

A very rough demo website has been setup and can be accessed via http://www.chefwirra.com.au. It is for telling designers what content is shown up on each page (except for homepage). By reading the about us page, designers can get some more info of Chef Wirra. However, the layout, theme color, font, etc are not set in stone. Visitors should be able to feel Chef Wirra restaurant's authentic Chinese cuisine and high hygiene standard. Home page of the website could be The "Our website is coming soon" description is shown on demo site but do not required to be presented on new design.

Some main pages design should be included: Home (landing page), About us, Menu (Dishes), Winelist, Gallery, Contact us. No HTML and coding required. The output should be well layered psd or png files with acceptable resolution for web use.

A few other website can be referred to are:

http://kelpmerachinese.com.au/
http://www.stone-lamp.com/
http://brimvale.com.au/
http://harvelrestaurant.com.au/
http://www.tilmorerestaurant.com.au/
http://www.thequill.com.au/

Industry/Entity Type

Restaurant

Requirements
Nice to have
• I expect designs of at least these webpages: homepage, menu page and contact us page. If you can provide "about us" page as well, it will probably help you win the competition. well layered psd or png file is my preference.
Should not have
• You don't have to make html/cs/js or any coding. All I need is just art design

```html
<!DOCTYPE html>
<html lang="en">
<head>
<meta charset="utf-8">
<title>Chef Wirra Chinese Restaurant</title>
<link href="https://fonts.googleapis.com/css2?family=Open+Sans:wght@400;600;700&family=Crimson+Text&display=swap" rel="stylesheet">
<style>
:root{
  --red:#d2432f;
  --red-dark:#b8321f;
  --red-line:#e8403a;
  --cream:#fbf3e4;
  --white:#fff;
  --ink:#333;
  --muted:#555;
  --rule:#e4e4e4;
  --footer:#000;
  --footer-text:#f2f2f2;
}
*{margin:0;padding:0;box-sizing:border-box}
html,body{width:945px;height:1200px;overflow:hidden}
body{position:relative;background:linear-gradient(180deg,#f25a3e 0%,var(--red) 35%,var(--red-dark) 100%);font-family:"Open Sans",sans-serif;color:var(--ink)}
.lattice{position:absolute;top:20px;width:82px;height:155px;border-radius:50%;background:radial-gradient(circle,#f6dcb0 0%,#f0c896 60%,rgba(240,200,150,0) 72%)}
.lattice.left{left:20px}
.lattice.right{right:20px}
.page{position:absolute;left:101px;top:0;width:743px;height:1200px;background:var(--white)}
.top-strip{height:25px;background:var(--cream)}
.header{position:relative;height:94px}
.brand{position:absolute;left:27px;top:30px;display:flex;align-items:center;gap:8px;font-weight:700;font-size:13px;color:#111;line-height:1.25;width:130px}
.brand-mark{width:14px;height:14px;background:#d8261c;flex:none}
.phone{position:absolute;right:25px;top:23px;font-size:16px;color:#222;display:flex;align-items:center;gap:7px}
.nav{position:absolute;right:25px;top:60px;display:flex;gap:29px;font-size:9px;letter-spacing:.3px;color:#333;list-style:none}
.hero{position:absolute;left:0;top:119px;width:743px;height:366px}
.hero-photo{position:absolute;inset:0;background:radial-gradient(ellipse at 30% 55%,#c98a52 0%,#7a3a2c 45%,#3f2328 100%);clip-path:polygon(0 0,100% 0,100% 92%,0 100%)}
.hero svg{position:absolute;left:0;top:0}
.section-title{position:absolute;left:24px;font-weight:700;font-size:12px;letter-spacing:.6px;color:#333;display:flex;align-items:center;gap:13px}
.section-title::after{content:"";width:126px;height:1px;background:var(--rule)}
.dots{position:absolute;right:25px;top:526px;display:flex;gap:7px}
.dots i{width:5px;height:5px;border-radius:50%;background:#ddd}
.dots i.on{background:#aaa}
.dish{position:absolute;top:560px;width:145px}
.dish-photo{height:126px}
.dish-caption{display:flex;justify-content:space-between;margin-top:17px;font-family:"Crimson Text",serif;font-size:12px;color:#555}
.about-photo{position:absolute;left:25px;top:786px;width:328px;height:208px;background:linear-gradient(180deg,#7a1f1a 0%,#a8612e 55%,#c9a042 100%)}
.about-text{position:absolute;left:389px;top:784px;width:325px;font-size:7.6px;line-height:15px;color:#444}
.about-text p{margin-bottom:7px}
.info{display:flex;margin-top:7px}
.info div{width:182px}
.info b{display:block;color:#222;font-weight:700}
.info .ind{padding-left:6px}
.footer{position:absolute;left:0;top:1034px;width:743px;height:166px;background:var(--footer);color:var(--footer-text);font-size:9.5px;line-height:19px}
.fcol{position:absolute;top:28px}
.fcol h3{font-size:9.5px;font-weight:700;letter-spacing:.5px;margin-bottom:6px;color:#fff}
.fcol h3.sub{margin-top:7px;margin-bottom:0}
.fcol p+p{margin-top:6px}
</style>
</head>
<body>
<div class="lattice left" role="img" aria-label="Decorative Chinese lattice window"></div>
<div class="lattice right" role="img" aria-label="Decorative Chinese lattice window"></div>

<main class="page">
  <div class="top-strip" role="img" aria-label="Cream band with plum blossom branches"></div>
  <header class="header">
    <div class="brand"><span class="brand-mark"></span><span>Chef Wirra Chinese Restaurant</span></div>
    <div class="phone">
      <svg width="18" height="18" viewBox="0 0 18 18"><circle cx="9" cy="9" r="8" fill="none" stroke="#222" stroke-width="1.6"/><path d="M7 5.5c-1.5 1.6-1.5 5.4 0 7l1.2-1.3c-.6-1-.6-3.4 0-4.4z" fill="#222"/></svg>
      08 8240 5173 &nbsp;/&nbsp; 08 9417 6352
    </div>
    <ul class="nav">
      <li>HOME</li><li>ABOUT US</li><li>MENU</li><li>WINE LIST</li><li>GALLERY</li><li>CONTACT US</li><li>KELPMERA COURT</li>
    </ul>
  </header>

  <section class="hero">
    <div class="hero-photo" role="img" aria-label="Pan-fried dumplings on a wooden plate with dipping sauce, spoon and chopsticks"></div>
    <svg width="743" height="366" viewBox="0 0 743 366"><line x1="0" y1="366" x2="743" y2="336.5" stroke="var(--red-line)" stroke-width="3"/></svg>
  </section>

  <h2 class="section-title" style="top:523px">FEATURED DISHES</h2>
  <div class="dots"><i></i><i class="on"></i><i></i><i></i></div>

  <article class="dish" style="left:25px"><div class="dish-photo" role="img" aria-label="Grilled skewers with rosemary" style="background:radial-gradient(circle,#4a5a2a,#1e1e22)"></div><div class="dish-caption"><span>Fugiat nulla sint</span><span>$30</span></div></article>
  <article class="dish" style="left:207px"><div class="dish-photo" role="img" aria-label="Stir-fried noodles in a wooden bowl" style="background:radial-gradient(circle,#6a4a2a,#a88a66)"></div><div class="dish-caption"><span>Daute irure dolor</span><span>$24</span></div></article>
  <article class="dish" style="left:390px"><div class="dish-photo" role="img" aria-label="Bowl of sliced banana and walnuts" style="background:radial-gradient(circle,#e8dcc0,#2a3a55)"></div><div class="dish-caption"><span>Officia deserunt mollit</span><span>$60</span></div></article>
  <article class="dish" style="left:573px"><div class="dish-photo" role="img" aria-label="Fried rice with vegetables in a wok" style="background:radial-gradient(circle,#c89a4a,#2a3038)"></div><div class="dish-caption"><span>Pim minim veniam</span><span>$17</span></div></article>

  <h2 class="section-title" style="top:750px">ABOUT US</h2>
  <div class="about-photo" role="img" aria-label="Private dining room with round table and red Chinese decor"></div>
  <div class="about-text">
    <p>Chef Wirra is named after its' executive chef, Mr Wirra. Chef Wirra had been in his career for nearly two decades before he moved to Australia 9 years ago. He settled in Adelaide then started his first restaurant, Kelpmera Court, in Norwood. Kelpmera Court has been running successfully for years due to Chef Wirra's talent of cooking.</p>
    <p>We are conveniently located at 2/47 Marden Lane, Kensal, within a few minutes driving distance from the city. We look forward to welcoming you at our restaurant!</p>
    <div class="info">
      <div>
        <b>Opening Hours</b>
        We are open 7 days
        <b class="ind">Lunch</b>
        <span class="ind" style="display:block">Monday to Friday 11:30am - 2:30pm</span>
        <span class="ind" style="display:block">Saturday to Sunday 11:00am - 3:00pm</span>
        <b class="ind">Dinner</b>
        <span class="ind" style="display:block">Monday to Sunday 6:00pm Until Late</span>
      </div>
      <div>
        <b>Address</b>
        2/47 Marden Lane<br>Kensal, SA, 5071<br>Australia
      </div>
    </div>
  </div>

  <footer class="footer">
    <div class="fcol" style="left:26px"><h3>ADDRESS</h3><p>2/47 Marden Lane<br>Kensal,<br>SA, 5071</p></div>
    <div class="fcol" style="left:209px"><h3>TRADING HOURS</h3><p>We are open 7 days</p><h3 class="sub">PHONE</h3><p style="margin-top:0">08 8240 5173<br>08 9417 6352</p></div>
    <div class="fcol" style="left:390px"><h3>LUNCH</h3><p>Monday to Friday<br>11:30am - 2:30pm</p><p>Saturday to Sunday<br>11:00am - 3:00pm</p></div>
    <div class="fcol" style="left:573px"><h3>DINNER</h3><p>Monday to Sunday<br>6:00pm Until Late</p></div>
  </footer>
</main>
</body>
</html>
```